Rainbow card

Looking for someone to design a card using rainbow theme and link 7 different promises of love to each color. The design will be used to either print a greeting card for valentines or flyer type layout to be framed.

Target Market(s)

Personal

Font styles to use
Script

Colors
eb1f27
f78f20
faee3e
9bcb3c
0655a3
6a429a
a64599

Requirements
Must have
• Rainbow
• The phrases to be included on each color are:
• red - I'll never leave you as long as you'll have me.
• orange - I'll never deny you my body.
• yellow - I'll never let you go to prison.
• green - I'll have a baby with you.
• blue - I'll marry you.
• Indigo - I'll always love you.
• Violet - I'll always stand by you and support you.
Nice to have
• Rainbow, love and loyalty significance

```html
<!DOCTYPE html>
<html lang="en">
<head>
<meta charset="utf-8">
<title>Rainbow of Promises</title>
<link rel="stylesheet" href="https://fonts.googleapis.com/css2?family=Dancing+Script:wght@600&display=swap">
<style>
  :root {
    --paper: #ffffff;
    --sky-deep: #4aa8ea;
    --sky-mid: #6cc0f2;
    --cloud: rgba(255,255,255,0.75);
    --red: #eb1f27;
    --orange: #f78f20;
    --yellow: #faee3e;
    --green: #9bcb3c;
    --blue: #0655a3;
    --indigo: #6a429a;
    --violet: #a64599;
    --text-red: #b0161d;
    --text-orange: #b8620f;
    --text-yellow: #a89a12;
    --text-green: #5f8a1e;
    --text-blue: #0655a3;
    --text-indigo: #5a3590;
    --text-violet: #8e3585;
    --leaf: rgba(158,216,74,0.85);
    --leaf-light: rgba(215,242,154,0.9);
    --flower-yellow: rgba(247,211,42,0.9);
    --flower-white: rgba(238,246,255,0.95);
    --stem: rgba(63,191,42,0.7);
    --dots: #3cc63c;
  }
  html, body {
    margin: 0;
    padding: 0;
    overflow: hidden;
    background: var(--paper);
  }
  .card {
    position: relative;
    width: 1200px;
    height: 953px;
    overflow: hidden;
    background: var(--paper);
  }
  .sky {
    position: absolute;
    left: 50px;
    top: 50px;
    width: 1100px;
    height: 855px;
    background:
      radial-gradient(ellipse 160px 70px at 180px 110px, var(--cloud), transparent 70%),
      radial-gradient(ellipse 220px 80px at 620px 60px, rgba(255,255,255,0.6), transparent 70%),
      radial-gradient(ellipse 200px 90px at 950px 160px, rgba(255,255,255,0.55), transparent 70%),
      radial-gradient(ellipse 260px 110px at 520px 420px, var(--cloud), transparent 70%),
      radial-gradient(ellipse 220px 90px at 880px 520px, rgba(255,255,255,0.6), transparent 70%),
      radial-gradient(ellipse 200px 90px at 180px 560px, rgba(255,255,255,0.55), transparent 70%),
      radial-gradient(ellipse 240px 80px at 640px 700px, rgba(255,255,255,0.5), transparent 70%),
      linear-gradient(180deg, var(--sky-mid), var(--sky-deep) 60%, var(--sky-mid));
    box-shadow: inset 0 0 22px 10px rgba(255,255,255,0.85);
    filter: blur(1px);
  }
  .rainbow {
    position: absolute;
    left: 0;
    top: 0;
    width: 1200px;
    height: 953px;
  }
  .art {
    position: absolute;
  }
  .art--leaves-left {
    left: 70px; top: 55px; width: 340px; height: 240px;
    background: radial-gradient(closest-side, var(--leaf-light), var(--leaf) 50%, transparent 100%);
  }
  .art--leaves-right {
    left: 950px; top: 55px; width: 195px; height: 355px;
    background: radial-gradient(closest-side, var(--leaf-light), var(--leaf) 50%, transparent 100%);
  }
  .art--yellow-flowers {
    left: 100px; top: 585px; width: 195px; height: 315px;
    background: radial-gradient(closest-side, var(--flower-yellow), var(--stem) 60%, transparent 100%);
  }
  .art--ferns {
    left: 835px; top: 765px; width: 150px; height: 130px;
    background: radial-gradient(closest-side, var(--leaf-light), var(--stem) 60%, transparent 100%);
  }
  .art--white-flowers {
    left: 995px; top: 575px; width: 145px; height: 320px;
    background: radial-gradient(closest-side, var(--flower-white), var(--stem) 65%, transparent 100%);
  }
  .promises {
    position: absolute;
    left: 340px;
    top: 464px;
    margin: 0;
    padding: 0;
    list-style: none;
    font-family: "Dancing Script", cursive;
    font-weight: 600;
    font-size: 32px;
    line-height: 52.5px;
    letter-spacing: 1.3px;
  }
  .promise {
    white-space: nowrap;
    -webkit-text-stroke: 0.6px rgba(40,20,30,0.55);
    text-shadow: 0 1px 1px rgba(255,255,255,0.6);
  }
  .promise--red { color: var(--text-red); }
  .promise--orange { color: var(--text-orange); }
  .promise--yellow { color: var(--text-yellow); }
  .promise--green { color: var(--text-green); }
  .promise--blue { color: var(--text-blue); }
  .promise--indigo { color: var(--text-indigo); }
  .promise--violet { color: var(--text-violet); }
  .ground-line {
    position: absolute;
    left: 200px;
    top: 874px;
    width: 950px;
    height: 0;
    border-top: 3px dotted var(--dots);
  }
</style>
</head>
<body>
<main class="card">
  <div class="sky"></div>

  <svg class="rainbow" viewBox="0 0 1200 953" aria-hidden="true">
    <defs>
      <clipPath id="sky-clip"><rect x="50" y="50" width="1100" height="855"/></clipPath>
      <filter id="soft-band" x="-10%" y="-10%" width="120%" height="120%">
        <feGaussianBlur stdDeviation="4"/>
      </filter>
    </defs>
    <g clip-path="url(#sky-clip)" filter="url(#soft-band)" fill="none" stroke-width="32">
      <path stroke="var(--red)"    d="M -50 455 Q 600 -75 1250 455"/>
      <path stroke="var(--orange)" d="M -50 492 Q 600 -64 1250 492"/>
      <path stroke="var(--yellow)" d="M -50 528 Q 600 -52 1250 528"/>
      <path stroke="var(--green)"  d="M -50 565 Q 600 -41 1250 565"/>
      <path stroke="var(--blue)"   d="M -50 601 Q 600 -29 1250 601"/>
      <path stroke="var(--indigo)" d="M -50 638 Q 600 -18 1250 638"/>
      <path stroke="var(--violet)" d="M -50 675 Q 600 -6 1250 675"/>
    </g>
  </svg>

  <div class="art art--leaves-left" role="img" aria-label="Sprigs of fresh green leaves hanging from the top left corner"></div>
  <div class="art art--leaves-right" role="img" aria-label="Sprigs of fresh green leaves hanging from the top right corner"></div>
  <div class="art art--yellow-flowers" role="img" aria-label="Tall stems of small yellow flowers with grass"></div>
  <div class="art art--ferns" role="img" aria-label="Small green ferns and grass"></div>
  <div class="art art--white-flowers" role="img" aria-label="Stems of white bell flowers"></div>

  <ul class="promises">
    <li class="promise promise--red">I'll never leave you as long as you'll have me.</li>
    <li class="promise promise--orange">I'll never deny you my body.</li>
    <li class="promise promise--yellow">I'll never let you go to prison.</li>
    <li class="promise promise--green">I'll have a baby with you.</li>
    <li class="promise promise--blue">I'll marry you.</li>
    <li class="promise promise--indigo">I'll always love you.</li>
    <li class="promise promise--violet">I'll always stand by you and support you.</li>
  </ul>

  <div class="ground-line"></div>
</main>
</body>
</html>
```